Melvin Otrasko Consulting Corporation
Independent Insurance and Reinsurance Consultants
Melvin Otrasko Consulting Corporation - Consulting
Creative Brief
Professional
Melvin Otrasko, MBA, CPCU
Insurance and Reinsurance Consultant
3816C Verlune Court Carlsbad, CA 92011
motrasko@motraskoadvise.com
www.motraskoadvise.com

```html
<!DOCTYPE html>
<html lang="en">
<head>
<meta charset="utf-8">
<title>Melvin Otrasko Consulting Corporation – Business Cards</title>
<link rel="stylesheet" href="https://fonts.googleapis.com/css2?family=Cormorant+Garamond:wght@500;600&family=Open+Sans:wght@400;600;700&display=swap">
<style>
  :root {
    --bg: #d9d9d9;
    --card-white: #ffffff;
    --brand-blue: #1d5aa8;
    --deep-blue: #174f9a;
    --mid-blue: #2f78c9;
    --light-blue: #5c9ee0;
    --ink: #3a3a3a;
    --muted: #6b7d92;
  }
  * { margin: 0; padding: 0; box-sizing: border-box; }
  html, body { width: 1200px; height: 794px; overflow: hidden; }
  body { background: var(--bg); position: relative; font-family: "Open Sans", sans-serif; color: var(--ink); }

  .card { position: absolute; border-radius: 16px; overflow: hidden; }
  .card--front { left: 391px; top: 67px; width: 466px; height: 305px; background: var(--card-white); }
  .card--back-light { left: 12px; top: 427px; width: 560px; height: 305px; background: var(--card-white); }
  .card--back-blue { left: 615px; top: 427px; width: 572px; height: 305px;
    background: radial-gradient(ellipse at 50% 55%, var(--light-blue) 0%, var(--mid-blue) 45%, var(--deep-blue) 100%); }

  .brand { position: absolute; left: 0; right: 0; text-align: center; z-index: 2; }
  .brand__name { font-family: "Cormorant Garamond", serif; font-weight: 500; color: var(--brand-blue);
    text-transform: uppercase; letter-spacing: 1px; line-height: 1; }
  .brand__tag { font-family: "Open Sans", sans-serif; color: var(--brand-blue); text-transform: uppercase;
    letter-spacing: 3.5px; line-height: 1; margin-top: 6px; }
  .card--front .brand { top: 26px; }
  .card--front .brand__name { font-size: 40px; }
  .card--front .brand__tag { font-size: 17px; }
  .card--back-light .brand { top: 118px; }
  .card--back-light .brand__name, .card--back-blue .brand__name { font-size: 44px; }
  .card--back-light .brand__tag, .card--back-blue .brand__tag { font-size: 18px; letter-spacing: 4px; }
  .card--back-blue .brand { top: 132px; }
  .card--back-blue .brand__name, .card--back-blue .brand__tag { color: #fff; }

  .contact { position: absolute; left: 22px; top: 114px; font-size: 11.5px; line-height: 1.45; z-index: 2; }
  .contact__address { margin-bottom: 6px; }
  .contact__row { display: flex; align-items: center; gap: 6px; }
  .contact__row svg { width: 10px; height: 10px; fill: var(--brand-blue); flex: none; }

  .person { position: absolute; left: 236px; top: 136px; z-index: 2; }
  .person__name { font-size: 16.5px; font-weight: 700; color: var(--brand-blue); }
  .person__role { font-size: 11.5px; color: var(--ink); margin-top: 2px; }

  .wave { position: absolute; left: 0; bottom: 0; width: 466px; height: 140px; z-index: 1; }

  .web { position: absolute; left: 0; right: 0; bottom: 14px; text-align: center; font-size: 12px; z-index: 2; }
  .web b { font-weight: 700; }
  .card--front .web { left: 22px; right: auto; text-align: left; bottom: 12px; font-size: 10.5px; color: #fff; }
  .card--back-light .web { color: var(--deep-blue); }
  .card--back-blue .web { color: #fff; }

  .emblem { position: absolute; z-index: 1; border-radius: 12px; }
  .card--front .emblem { left: 300px; top: 228px; width: 110px; height: 66px;
    background: radial-gradient(ellipse, rgba(255,255,255,0.22), rgba(255,255,255,0)); }
  .card--back-light .emblem { left: 36px; top: 18px; width: 180px; height: 250px;
    background: radial-gradient(ellipse, rgba(180,190,200,0.35), rgba(255,255,255,0)); }
  .card--back-blue .emblem { left: 225px; top: 95px; width: 140px; height: 175px;
    background: radial-gradient(ellipse, rgba(150,200,240,0.35), rgba(255,255,255,0)); }
</style>
</head>
<body>

<section class="card card--front">
  <div class="brand">
    <div class="brand__name">Melvin Otrasko</div>
    <div class="brand__tag">Consulting Corporation</div>
  </div>

  <div class="contact">
    <div class="contact__address">3816C Verlune Court<br>Carlsbad, CA 92011</div>
    <div class="contact__row"><svg viewBox="0 0 10 10"><path d="M2 0.5 L3.6 2.5 L2.8 3.6 Q4 6 6.4 7.2 L7.5 6.4 L9.5 8 L8.3 9.5 Q3.5 9 0.5 1.7 Z"/></svg>6195550142</div>
    <div class="contact__row"><svg viewBox="0 0 10 10"><rect x="2.5" y="0.5" width="5" height="9" rx="1"/></svg>6195550187</div>
    <div class="contact__row"><svg viewBox="0 0 10 10"><rect x="0.5" y="3" width="9" height="5" rx="1"/><rect x="2.5" y="0.5" width="5" height="3"/></svg>7605550163</div>
    <div class="contact__row"><svg viewBox="0 0 10 10"><circle cx="5" cy="5" r="4.5"/></svg>motrasko@motraskoadvise.com</div>
  </div>

  <div class="person">
    <div class="person__name">Melvin Otrasko, MBA, CPCU</div>
    <div class="person__role">Insurance and Reinsurance Consultant</div>
  </div>

  <svg class="wave" viewBox="0 0 466 140" preserveAspectRatio="none" aria-hidden="true">
    <defs>
      <linearGradient id="waveBlue" x1="0" y1="0" x2="1" y2="1">
        <stop offset="0" stop-color="#3a86d4"/>
        <stop offset="1" stop-color="#174f9a"/>
      </linearGradient>
    </defs>
    <path d="M0 60 C120 130 300 20 466 10 L466 140 L0 140 Z" fill="#9cc4ea"/>
    <path d="M0 78 C130 140 300 40 466 26 L466 140 L0 140 Z" fill="#ffffff"/>
    <path d="M0 90 C140 145 300 55 466 40 L466 140 L0 140 Z" fill="url(#waveBlue)"/>
  </svg>
  <div class="emblem" role="img" aria-label="Faint scales of justice emblem"></div>

  <div class="web">www.motraskoadvise.com</div>
</section>

<section class="card card--back-light">
  <div class="emblem" role="img" aria-label="Faint scales of justice emblem"></div>
  <div class="brand">
    <div class="brand__name">Melvin Otrasko</div>
    <div class="brand__tag">Consulting Corporation</div>
  </div>
  <div class="web">www.<b>motraskoadvise</b>.com</div>
</section>

<section class="card card--back-blue">
  <div class="emblem" role="img" aria-label="Faint scales of justice emblem"></div>
  <div class="brand">
    <div class="brand__name">Melvin Otrasko</div>
    <div class="brand__tag">Consulting Corporation</div>
  </div>
  <div class="web">www.<b>motraskoadvise</b>.com</div>
</section>

</body>
</html>
```